Leadership Training Business Needs a business card design

We need a business card designed for our company based in Auckland, New Zealand called Kestrel Pathway Services. We conduct a variety of residential programmes that provide for differnet management levels. These programmes are designed to familiarise managers with important leadership concepts and techniques. This learning is reinforced through the provision of real workplace feedback and the use of action learning opportunities (experiential exercises) to develop the participants' leadership skills and potential. We would like to add our tag line which is:
Inspires Direction - Instils Values - Delivers Results
We would like the card to be a white background but would consider a different background colour on the back. Possibly include the following words on the back:
- Organisational Development
- Positive Cultural Change
- Leadership Programmes
- Practical Development "Tools"
- Crew Guidance Matrix
- 360o degree Assessments
- Strengths Based Training
- Coaching and Mentoring

Must have
• Company Name, logo, contact details, website address and email.
• Persons name and their title

```html
<!DOCTYPE html>
<html lang="en">
<head>
<meta charset="utf-8">
<title>Kestrel Pathway Services – Business Card</title>
<link rel="stylesheet" href="https://fonts.googleapis.com/css2?family=Source+Sans+3:ital,wght@0,400;0,600;0,700;1,400&display=swap">
<style>
  :root {
    --canvas: #ececec;
    --white: #ffffff;
    --brand-blue: #0b5fa0;
    --brand-blue-text: #1a6fb5;
    --tagline-blue: #0d5ea6;
    --ink: #1f1f1f;
    --sky: #bfe3f8;
    --sky-soft: #e6f4fc;
    --back-light: #86cdf2;
    --back-deco: #1a8fd0;
    --mark: #2f9ad8;
  }
  * { box-sizing: border-box; margin: 0; padding: 0; }
  html, body {
    width: 1200px; height: 1200px; overflow: hidden;
    background: var(--canvas);
    font-family: "Source Sans 3", "Myriad Pro", Arial, sans-serif;
  }
  .canvas { position: relative; width: 1200px; height: 1200px; }

  .card {
    position: absolute; left: 236px; width: 848px; height: 482px; overflow: hidden;
  }
  .card--front { top: 82px; background: var(--white); }
  .card--back  { top: 642px; background: var(--brand-blue); }

  .card__decoration {
    position: absolute; left: 0; top: 0; width: 360px; height: 100%;
  }
  .card--front .card__decoration {
    background: radial-gradient(ellipse at 25% 35%, var(--sky) 0%, var(--sky-soft) 55%, rgba(255,255,255,0) 80%);
  }
  .card--back .card__decoration {
    background: radial-gradient(ellipse at 25% 40%, var(--back-deco) 0%, rgba(26,143,208,0.45) 55%, rgba(11,95,160,0) 82%);
  }

  .brand { position: absolute; text-align: center; }
  .brand__mark { display: block; margin: 0 auto; border-radius: 50%; background: var(--mark); }
  .brand__name { display: block; font-weight: 400; line-height: 1.1; white-space: nowrap; }
  .brand__sub  { display: block; font-weight: 400; line-height: 1.1; white-space: nowrap; }

  .card--front .brand { left: 420px; width: 360px; top: 14px; }
  .card--front .brand__mark { width: 132px; height: 132px; margin-bottom: 30px; }
  .card--front .brand__name { font-size: 28px; color: var(--ink); }
  .card--front .brand__sub  { font-size: 27px; color: var(--brand-blue-text); margin-top: 2px; }

  .name-band {
    position: absolute; left: 335px; top: 300px; width: 513px; height: 53px;
    background: var(--brand-blue); color: var(--white);
    display: flex; align-items: center; justify-content: center; gap: 14px;
  }
  .name-band__name  { font-weight: 700; font-size: 34px; }
  .name-band__sep   { font-size: 34px; font-weight: 400; }
  .name-band__title { font-style: italic; font-size: 27px; }

  .tagline {
    position: absolute; left: 100px; top: 420px;
    font-weight: 700; font-size: 25px; color: var(--tagline-blue); letter-spacing: 0.4px;
    white-space: nowrap;
  }

  .card--back .brand { left: 500px; width: 310px; top: 32px; }
  .card--back .brand__mark { width: 104px; height: 104px; margin-bottom: 14px; }
  .card--back .brand__name { font-size: 22px; color: var(--white); }
  .card--back .brand__sub  { font-size: 21px; color: var(--back-light); }

  .services {
    position: absolute; left: 0; top: 310px; width: 848px;
    display: grid; grid-template-columns: 488px 1fr; column-gap: 22px; row-gap: 12px;
    font-weight: 700; font-size: 20.5px; letter-spacing: 0.4px; line-height: 25px;
  }
  .services__primary { text-align: right; color: var(--back-light); white-space: nowrap; }
  .services__secondary { color: var(--white); white-space: nowrap; }
</style>
</head>
<body>
<main class="canvas">

  <section class="card card--front" aria-label="Business card front">
    <div class="card__decoration" role="img" aria-label="Large soft light-blue brand decoration"></div>
    <div class="brand">
      <span class="brand__mark" aria-hidden="true"></span>
      <span class="brand__name">Kestrel Pathway Services</span>
      <span class="brand__sub">Leadership Programmes</span>
    </div>
    <div class="name-band">
      <span class="name-band__name">Daniel Ashworth</span>
      <span class="name-band__sep">|</span>
      <span class="name-band__title">Facilitator</span>
    </div>
    <p class="tagline">Inspires Direction | Instils Values | Delivers Results</p>
  </section>

  <section class="card card--back" aria-label="Business card back">
    <div class="card__decoration" role="img" aria-label="Large soft blue brand decoration"></div>
    <div class="brand">
      <span class="brand__mark" aria-hidden="true"></span>
      <span class="brand__name">Kestrel Pathway Services</span>
      <span class="brand__sub">Leadership Programmes</span>
    </div>
    <div class="services">
      <span class="services__primary">Organisational Development</span>
      <span class="services__secondary">Positive Cultural Change</span>
      <span class="services__primary">Practical Development "Tools"</span>
      <span class="services__secondary">Leadership Programmes</span>
      <span class="services__primary">Crew Guidance Matrix</span>
      <span class="services__secondary">360<sup>o</sup> degree Assessments</span>
      <span class="services__primary">Strengths Based Training</span>
      <span class="services__secondary">Coaching and Mentoring</span>
    </div>
  </section>

</main>
</body>
</html>
```